Doctors clinic requires stationary designed

We require various types of stationary to be design based on the logo (attached). We require the following:
- Letterhead (A4 Portrait)
- Business Card (must include UV spot on rear)
- With compliments slip (DL Landscape)
- Appointments card (Folded A6)

We are a young clinical practice which boasts a modern and sophisticated approach to medicine so we require something which feels fresh and modern. Please include colours represented in the logo (contrasting teal and grey). We are calling for creative minds to put forth their ideas and we will be actively providing feedback on all designs.

thank you

Clinic

```html
<!DOCTYPE html>
<html lang="en">
<head>
<meta charset="utf-8">
<title>Letterhead – Dr Clara Hensley</title>
<link href="https://fonts.googleapis.com/css2?family=Source+Sans+3:wght@400;600;700&display=swap" rel="stylesheet">
<style>
  :root {
    --teal: #15968f;
    --teal-faint: #e7efee;
    --paper: #f6f7f7;
    --backdrop: #dce8e8;
    --ink: #555b5c;
    --white: #ffffff;
  }
  * { box-sizing: border-box; margin: 0; padding: 0; }
  html, body { width: 1035px; height: 1200px; overflow: hidden; }
  body {
    background: var(--backdrop);
    font-family: "Source Sans 3", "Helvetica Neue", Arial, sans-serif;
    color: var(--ink);
  }
  .letterhead {
    position: absolute;
    left: 105px; top: 20px;
    width: 824px; height: 1160px;
    background: var(--paper);
    overflow: hidden;
  }
  .masthead {
    position: absolute; left: 0; top: 0;
    width: 100%; height: 183px;
    background: var(--teal);
    color: var(--white);
  }
  .brand {
    position: absolute; left: 58px; top: 66px;
    display: flex; align-items: center; gap: 14px;
  }
  .brand-mark {
    width: 52px; height: 52px; border-radius: 50%;
    border: 2px solid var(--white);
  }
  .brand-name { font-size: 22px; font-weight: 600; line-height: 1.05; letter-spacing: -0.3px; }
  .brand-role { font-size: 13px; font-weight: 600; line-height: 1.2; }
  .contact {
    position: absolute; left: 567px; top: 66px;
    border-left: 1px solid rgba(255,255,255,0.7);
    padding-left: 16px; height: 66px;
    font-size: 11px; font-weight: 600;
    display: flex; flex-direction: column; justify-content: center; gap: 5px;
  }
  .contact-row { display: flex; align-items: center; gap: 8px; }
  .contact-row svg { width: 12px; height: 12px; flex: none; }
  .watermark-ring {
    position: absolute; left: 390px; top: 720px;
    width: 520px; height: 520px; border-radius: 50%;
    border: 16px solid var(--teal-faint);
  }
  .letter-body {
    position: absolute; left: 137px; top: 322px;
    width: 580px;
    font-size: 14.5px; line-height: 18.5px;
  }
  .letter-body p { margin-bottom: 18.5px; }
  .signature {
    width: 115px; height: 58px; margin-top: 40px;
    background: linear-gradient(90deg, #d9dcdc, #eceeee);
    border-radius: 4px;
  }
  .signatory-name { font-size: 14.5px; margin-top: 6px; line-height: 17px; }
  .signatory-role { font-size: 13px; line-height: 16px; }
  .footer-band {
    position: absolute; left: 0; bottom: 0;
    width: 100%; height: 60px;
    background: var(--teal); color: var(--white);
    font-size: 12.5px;
    display: flex; align-items: center; justify-content: center;
  }
</style>
</head>
<body>
  <main class="letterhead">
    <header class="masthead">
      <div class="brand">
        <span class="brand-mark"></span>
        <div>
          <div class="brand-name">Dr Clara Hensley</div>
          <div class="brand-role">Obstetrician and Gynaecologist</div>
        </div>
      </div>
      <div class="contact">
        <div class="contact-row">
          <svg viewBox="0 0 12 12" fill="none" stroke="#fff" stroke-width="1"><rect x="3" y="0.5" width="6" height="11" rx="1"/><line x1="5" y1="9.5" x2="7" y2="9.5"/></svg>
          <span>Tel: 9612 4410 &nbsp;|&nbsp; Fax: 9612 4410</span>
        </div>
        <div class="contact-row">
          <svg viewBox="0 0 12 12" fill="none" stroke="#fff" stroke-width="1"><rect x="0.5" y="2.5" width="11" height="7"/><polyline points="0.5,2.5 6,7 11.5,2.5"/></svg>
          <span>clara@drclarahensley.com.au</span>
        </div>
        <div class="contact-row">
          <svg viewBox="0 0 12 12" fill="none" stroke="#fff" stroke-width="1"><circle cx="6" cy="6" r="5.5"/><ellipse cx="6" cy="6" rx="2.5" ry="5.5"/><line x1="0.5" y1="6" x2="11.5" y2="6"/></svg>
          <span>drclarahensley.com.au</span>
        </div>
      </div>
    </header>

    <div class="watermark-ring" aria-hidden="true"></div>

    <section class="letter-body">
      <p>Lorem ipsum dolor sit amet,</p>
      <p>Consectetur adipiscing elit. Duis non fermentum dui. Phasellus erat tortor, faucibus vitae dui nec, lobortis aliquet purus. Integer lacinia nibh nec mi dignissim varius. In vulputate condimentum turpis, non volutpat erat condimentum posuere. In nec lorem ac felis ornare posuere. Donec non justo vulputate, laoreet justo ac, viverra turpis. Vivamus vitae sapien eget dui pellentesque pulvinar.</p>
      <p>Nullam ultrices fringilla nisi. Proin vel ipsum rhoncus, vehicula erat nec, viverra mi. Maecenas convallis turpis ac elit ornare, nec eleifend dui vehicula. Etiam rutrum dui ipsum, ac dignissim est pretium nec. Nullam venenatis lacus eget neque tempus maximus. Fusce porttitor tellus eu efficitur scelerisque. Class aptent taciti sociosqu ad litora torquent per conubia nostra, per inceptos himenaeos.</p>
      <p>Sed ornare sodales enim, ac viverra arcu sodales eget. Sed commodo nunc at tincidunt laoreet. Mauris pellentesque ex nulla, eu mollis neque sodales nec. Suspendisse potenti.</p>
      <p>Duis eu libero a massa,</p>
      <div class="signature" role="img" aria-label="Handwritten signature"></div>
      <div class="signatory-name">Dr. Clara Hensley</div>
      <div class="signatory-role">Obstetrician and Gynaecologist</div>
    </section>

    <footer class="footer-band">Northgate Private Hospital, Suite 4 Spec. Med. Centre (West) - Harbour Ave, Northgate</footer>
  </main>
</body>
</html>
```